Bref créative
Business card and stationary for Lesson Lantern
Bright & Fun-filled
Marla Vettington
Founder
I do not want the address on my busines card. Address is;
Suite 514- 2870 West Orchard Avenue, Burnaby, BC Canada V5K 2R9
1-877- GO LEARN
info@lessonlantern-example.com
lessonlantern-example.com
B.Ed, MA Ed, TESL
In Home Tutoring
Certified Teachers
K-12 (All Subjects)
Know Any Great Teachers? We're looking.
Also: Franchise Opportunities Available!

```html
<!DOCTYPE html>
<html lang="en">
<head>
<meta charset="utf-8">
<title>Lesson Lantern Stationery</title>
<link href="https://fonts.googleapis.com/css2?family=Open+Sans:wght@400;600;700;800&display=swap" rel="stylesheet">
<style>
:root{
  --bg:#e9e9e9;
  --paper:#ffffff;
  --blue:#1f8fd6;
  --dark:#2a2a2a;
  --ink:#444;
  --muted:#8a8a8a;
  --faint:#e6eaf0;
  --rule:#b9b9b9;
}
*{box-sizing:border-box;margin:0;padding:0}
html,body{width:1200px;height:521px;overflow:hidden;background:var(--bg);font-family:"Open Sans",Arial,sans-serif;color:var(--ink)}
.stage{position:relative;width:1200px;height:521px}
.option-label{position:absolute;top:6px;font-weight:700;font-size:24px;color:var(--dark)}
.sheet{position:absolute;background:var(--paper);box-shadow:0 2px 6px rgba(0,0,0,.25);overflow:hidden}
.brand{display:flex;align-items:center;gap:5px;color:var(--blue);font-weight:800;white-space:nowrap}
.brand .dot{border-radius:50%;background:var(--blue);flex:none}
.band{position:absolute;left:0;right:0;bottom:0;width:100%}
.tiny{font-size:5px;line-height:7px;color:var(--muted)}

/* letterhead */
.letterhead{left:26px;top:52px;width:310px;height:460px}
.letterhead .brand{position:absolute;left:0;right:0;top:18px;justify-content:center;font-size:12px}
.letterhead .brand .dot{width:9px;height:9px}
.letterhead .mark-area{position:absolute;left:40px;top:150px;width:180px;height:180px;border-radius:50%;border:10px solid var(--faint)}
.letterhead .footer-text{position:absolute;left:0;right:0;bottom:24px;text-align:center}

/* fax */
.fax{left:386px;top:52px;width:312px;height:460px}
.fax .brand{position:absolute;left:18px;top:20px;font-size:10px}
.fax .brand .dot{width:8px;height:8px}
.fax .contact{position:absolute;left:165px;top:14px}
.fax h1{position:absolute;left:18px;top:78px;font-size:22px;font-weight:400;color:var(--dark);letter-spacing:1px}
.fax-fields{position:absolute;left:18px;right:18px;top:118px;display:grid;grid-template-columns:1fr 1fr;column-gap:10px;row-gap:11px}
.fax-field{display:flex;align-items:flex-end;font-size:5px;color:var(--ink);border-bottom:1px solid var(--rule);height:12px}
.fax-rule{position:absolute;left:18px;right:18px;top:222px;border-top:1px solid var(--rule)}
.fax-checks{position:absolute;left:18px;right:18px;top:232px;display:flex;justify-content:space-between;font-size:5px}
.fax-checks span::before{content:"";display:inline-block;width:6px;height:6px;border:1px solid var(--rule);margin-right:3px;vertical-align:middle}

/* envelopes */
.envelope-back{left:772px;top:52px;width:418px;height:104px}
.envelope-front{left:800px;top:116px;width:390px;height:132px}
.envelope-front .brand{position:absolute;left:0;width:130px;top:18px;justify-content:center;font-size:9px}
.envelope-front .brand .dot{width:7px;height:7px}
.envelope-front .return{position:absolute;left:14px;top:34px;font-size:4px;line-height:6px}
.envelope-front .mark-area{position:absolute;left:255px;top:20px;width:82px;height:82px;border-radius:50%;border:6px solid var(--faint)}

/* cards */
.card{top:372px;width:200px;height:138px}
.card-front{left:762px}
.card-back{left:980px}
.card-front .brand{position:absolute;left:0;right:0;top:16px;justify-content:center;font-size:9px}
.card-front .brand .dot{width:7px;height:7px}
.card-front .person{position:absolute;left:0;right:0;top:52px;text-align:center}
.person .name{font-size:6px;font-weight:700;color:var(--dark)}
.person .role{font-size:4.5px;color:var(--muted)}
.card-front .details{position:absolute;left:18px;right:18px;top:70px;display:grid;grid-template-columns:1fr 1fr;column-gap:6px;font-size:4.5px;line-height:6.5px}
.card-back .top-lines{position:absolute;left:0;right:0;top:14px;text-align:center;font-size:4.5px;line-height:7px;color:var(--ink)}
.card-back .bottom-lines{position:absolute;left:0;right:0;top:84px;text-align:center;font-size:4.5px;line-height:7px;color:var(--blue);font-weight:700}
</style>
</head>
<body>
<div class="stage">
  <div class="option-label" style="left:132px">Option_1</div>
  <div class="option-label" style="left:504px">Option_2</div>

  <section class="sheet letterhead">
    <div class="brand"><span class="dot"></span>Lesson Lantern</div>
    <div class="mark-area" role="img" aria-label="Faint brand emblem decoration"></div>
    <div class="footer-text tiny">
      T: 1-800-555-0142 &nbsp; E: info@lessonlantern-example.com &nbsp; W: lessonlantern-example.com<br>
      Suite 514- 2870 West Orchard Avenue, Fernvale, ON Canada K0X 1Z9
    </div>
    <svg class="band" height="14" viewBox="0 0 310 14" preserveAspectRatio="none">
      <rect x="0" y="6" width="310" height="5" fill="var(--blue)"/>
      <polygon points="262,14 310,0 310,14" fill="var(--dark)"/>
    </svg>
  </section>

  <section class="sheet fax">
    <div class="brand"><span class="dot"></span>Lesson Lantern</div>
    <div class="contact tiny">
      Suite 514- 2870 West Orchard Avenue<br>
      Fernvale, ON Canada K0X 1Z9<br>
      T: 1-800-555-0142<br>
      E: info@lessonlantern-example.com<br>
      W: lessonlantern-example.com
    </div>
    <h1>FAX</h1>
    <div class="fax-fields">
      <div class="fax-field">To:</div><div class="fax-field">From:</div>
      <div class="fax-field">Fax:</div><div class="fax-field">Pages:</div>
      <div class="fax-field">Phone:</div><div class="fax-field">Date:</div>
      <div class="fax-field">Re:</div><div class="fax-field">CC:</div>
    </div>
    <div class="fax-rule"></div>
    <div class="fax-checks">
      <span>Urgent</span><span>For Review</span><span>Please Comment</span><span>Please Reply</span><span>Please Recycle</span>
    </div>
  </section>

  <section class="sheet envelope-back">
    <svg width="418" height="104" viewBox="0 0 418 104">
      <polyline points="0,0 150,64 268,64 418,0" fill="none" stroke="var(--rule)" stroke-width="1"/>
    </svg>
  </section>

  <section class="sheet envelope-front">
    <div class="brand"><span class="dot"></span>Lesson Lantern</div>
    <div class="return tiny">Suite 514- 2870 West Orchard Avenue, Fernvale, ON Canada K0X 1Z9</div>
    <div class="mark-area" role="img" aria-label="Faint brand emblem decoration"></div>
    <svg class="band" height="12" viewBox="0 0 390 12" preserveAspectRatio="none">
      <rect x="0" y="5" width="390" height="4" fill="var(--blue)"/>
      <polygon points="350,12 390,0 390,12" fill="var(--dark)"/>
    </svg>
  </section>

  <section class="sheet card card-front">
    <div class="brand"><span class="dot"></span>Lesson Lantern</div>
    <div class="person">
      <div class="name">Marla Vettington</div>
      <div class="role">Founder &middot; B.Ed, MA Ed, TESL</div>
    </div>
    <div class="details tiny">
      <div>T: 1-800-555-0142<br>Certified Teachers</div>
      <div>info@lessonlantern-example.com<br>lessonlantern-example.com</div>
    </div>
    <svg class="band" height="10" viewBox="0 0 200 10" preserveAspectRatio="none">
      <rect x="0" y="4" width="200" height="4" fill="var(--blue)"/>
      <polygon points="170,10 200,0 200,10" fill="var(--dark)"/>
    </svg>
  </section>

  <section class="sheet card card-back">
    <div class="top-lines">
      In Home Tutoring &middot; Certified Teachers<br>
      K-12 (All Subjects)
    </div>
    <div class="bottom-lines">
      Know Any Great Teachers? We're looking.<br>
      Also: Franchise Opportunities Available!
    </div>
    <svg class="band" height="10" viewBox="0 0 200 10" preserveAspectRatio="none">
      <rect x="0" y="4" width="200" height="4" fill="var(--blue)"/>
      <polygon points="170,10 200,0 200,10" fill="var(--dark)"/>
    </svg>
  </section>
</div>
</body>
</html>
```